We have a small 501C Non-Profit, called Youngsters Unite. The non-profit was started by my son and his friends during the Gulf Oil Spill. We would like to update the website that currently sits on Domivault.com. I'm not sure how we transfer over the domain or get them to host it with your new design. I've attached a link of the old site that we developed. We are open to any ideas regarding hosting.

We would basically like a look that is youth (teen, college age) oriented that will drive teens and donors to the site. Our goal is to get onto Plixa Drives, get grants and make major donations with little to no administration expense. We will get sponsors to pay for the administration costs. So we will be looking for sponsors to support the overhead and 100% of donor money will go to causes important to teens.

http://www.youngstersunite.org

Target Market(s)

Teenagers and Individual Sponsors. Adults that want to help teens with an important cause.

Industry/Entity Type

Non-Profit

Requirements
Must have
• We are very open to ideas. It would be good to have a:

Home-with Mission Statement and Photos or Graphics
Donate-100% of Donations Go To Causes (with Coinvo Link)
Become A Sponsor-Insert Contact Information In This Section.
How It All Got Started -with info, articles, events, video, etc. from Gulf Oil Spill, Our Founder photo.
Contact-Change phone number to 555-804-2739. Keep e-mail and mailing the same.

You can use some existing photos from current site if you would like. All the Recent Event Photos, Founder Photo, 3 people holding check photo were all taken by me so there are no rights issues with those.

YU Mission Statement:

To demonstrate to the world that Youngsters Unite about the environment, each other and world peace through fund raising and other philanthropic efforts.
Nice to have
• Youngsters Unite Logo If Possible

Photo of 3 people, holding check, from existing home page in new History Section.

Kindpaw League Story and Logo in History Section

WRX Video in History Section

Helpio4
http://www.helpio4.net/stories/youth-launches-charity-to-fund-relief-for-wildlife-harmed-by-coastal-slick.html
Should not have
• Delete Blog Section
Delete Founder Section
Delete Recent Events
Delete How To Get Involved

```html
<!DOCTYPE html>
<html lang="en">
<head>
<meta charset="utf-8">
<title>Youngsters Unite</title>
<link rel="stylesheet" href="https://fonts.googleapis.com/css2?family=Montserrat:wght@300;400;700&family=Arimo:wght@400&display=swap">
<style>
:root{
  --ink:#111;
  --text:#222;
  --rule:#2c4f9e;
  --sky-mid:#bfdcf3;
  --panel:#f7f7f7;
  --panel-edge:#c5dcef;
  --frame:#b4b4b4;
  --caption:rgba(0,0,0,.82);
  --accent-red:#d7261f;
  --accent-orange:#ee7a24;
  --accent-green:#6b7a3d;
  --plixa:#3b5998;
  --helpio:#2f8fc4;
}
*{margin:0;padding:0;box-sizing:border-box}
html,body{width:1200px;height:1046px;overflow:hidden}
body{position:relative;background:#fff;font-family:"Arimo",Arial,sans-serif;color:var(--text)}
.sky{position:absolute;left:0;top:0;width:1200px;height:740px;
  background:
    radial-gradient(ellipse 320px 60px at 40px 270px,rgba(30,80,190,.85),transparent 70%),
    radial-gradient(ellipse 260px 50px at 1160px 240px,rgba(40,100,200,.7),transparent 70%),
    radial-gradient(ellipse 500px 120px at 150px 480px,rgba(60,130,215,.45),transparent 70%),
    radial-gradient(ellipse 600px 140px at 1050px 520px,rgba(60,130,215,.4),transparent 70%),
    linear-gradient(180deg,var(--sky-mid) 0,#d6e9f8 60%,#fff 100%);}
.masthead{position:absolute;left:0;top:0;width:1200px;height:128px;
  background:linear-gradient(90deg,#c8e0f6 0,#f4f9fe 35%,#f4f9fe 65%,#c8e0f6 100%)}
.brand{position:absolute;left:410px;top:42px;display:flex;align-items:center;gap:12px;
  font-family:"Montserrat",sans-serif;font-weight:400;font-size:33px;color:var(--ink)}
.brand-mark{width:64px;height:64px;border-radius:50%;background:#3a64b6;border:3px solid #1b2c55}
.main-nav{position:absolute;left:0;top:128px;width:1200px;height:50px;background:#fff;
  border-top:2px solid #cfe2f2;border-bottom:2px solid #cfe2f2;display:flex;justify-content:center}
.main-nav a{font-family:"Arimo",sans-serif;font-size:15px;color:var(--ink);text-decoration:none;
  padding:0 26px;line-height:38px;margin-top:4px;border-left:1px solid #ccc}
.main-nav a:first-child{border-left:none}
.panel{position:absolute;background:var(--panel);border:2px solid var(--panel-edge);border-radius:6px;
  box-shadow:0 0 0 1px #fff inset}
.hero{left:117px;top:213px;width:967px;height:320px;
  background:radial-gradient(circle,#ddd 1.2px,transparent 1.6px) 0 0/32px 32px,var(--panel)}
.hero-title{position:absolute;left:76px;top:27px;width:420px;text-align:center;white-space:nowrap;
  font-family:"Montserrat",sans-serif;font-weight:700;font-size:32px;line-height:38px;color:var(--ink)}
.causes{position:absolute;left:76px;top:118px;width:420px;border-top:1px solid var(--rule);
  border-bottom:1px solid var(--rule);padding:6px 19px 8px;
  font-family:"Montserrat",sans-serif;font-weight:300;font-size:25px;line-height:41px;color:var(--ink)}
.causes-line{display:flex;justify-content:space-between;white-space:nowrap}
.partner{position:absolute;top:246px;font-family:"Montserrat",sans-serif;font-weight:700;font-size:18px;white-space:nowrap}
.partner.lakou{left:136px;color:var(--accent-orange)}
.partner.wingfield{left:290px;color:var(--accent-green)}
.photo{position:absolute;border:3px solid var(--frame)}
.hero-photo{left:568px;top:14px;width:380px;height:284px;
  background:linear-gradient(160deg,#e6e2d8 0,#b9a58c 45%,#6a5a46 100%)}
.mission{left:117px;top:571px;width:968px;height:155px;background:linear-gradient(#fff,#f3f3f3)}
.mission h2{position:absolute;left:268px;top:18px;width:420px;text-align:center;border-bottom:1px solid var(--rule);
  font-family:"Montserrat",sans-serif;font-weight:700;font-size:30px;padding-bottom:8px;color:var(--ink)}
.mission p{position:absolute;left:20px;top:76px;width:924px;text-align:center;font-size:17px;line-height:30px;color:var(--ink);letter-spacing:-.2px}
.card{position:absolute;top:762px;height:194px;overflow:hidden}
.card.group{left:120px;width:303px;background:linear-gradient(180deg,#d9d2b8 0,#a89a84 50%,#5d5749 100%)}
.card.founder{left:453px;width:259px;background:linear-gradient(180deg,#d7dde4 0,#9fae9a 45%,#4f6242 100%)}
.card span{position:absolute;left:0;right:0;bottom:6px;height:37px;background:var(--caption);color:#fff;
  font-size:15px;line-height:37px;text-align:center}
.social{position:absolute;font-family:"Montserrat",sans-serif;font-size:15px;color:var(--ink);white-space:nowrap}
.social-mark{position:absolute;font-family:"Montserrat",sans-serif;font-weight:700;white-space:nowrap}
.vidora{left:968px;top:772px;font-size:26px;color:var(--accent-red)}
.plixa{left:965px;top:834px;display:flex;align-items:center;gap:6px;font-size:17px;color:var(--plixa)}
.plixa i{width:16px;height:16px;background:var(--plixa);display:block}
.helpio{left:808px;top:914px;display:flex;align-items:center;gap:8px;font-size:30px;color:var(--helpio)}
.helpio i{width:14px;height:14px;border-radius:50%;background:var(--helpio);display:block}
.site-footer{position:absolute;left:119px;top:997px;width:964px;font-size:12px;color:var(--ink);display:flex;justify-content:space-between}
.site-footer nav a{color:var(--ink);text-decoration:none}
.site-footer nav b{font-weight:400;margin:0 8px}
</style>
</head>
<body>
<div class="sky"></div>
<header class="masthead">
  <div class="brand">Youngsters Unite<span class="brand-mark"></span></div>
</header>
<nav class="main-nav">
  <a href="#">HOME</a><a href="#">DONATE</a><a href="#">BECOME A SPONSOR</a><a href="#">HOW IT ALL GOT STARTED</a><a href="#">CONTACT</a>
</nav>

<section class="panel hero">
  <h1 class="hero-title">HELPING THE OTHERS<br>AROUND THE WORLD</h1>
  <div class="causes">
    <div class="causes-line"><span>Disaster Relief</span><span>-</span><span>Environment</span></div>
    <div class="causes-line"><span>Water</span><span>-</span><span>Hunger</span><span>-</span><span>Medical</span></div>
  </div>
  <div class="partner lakou">Lakou Health</div>
  <div class="partner wingfield">Wingfield</div>
  <div class="photo hero-photo" role="img" aria-label="Teen volunteers collecting donations in a bowl under an event tent"></div>
</section>

<section class="panel mission">
  <h2>MISSION STATEMENT</h2>
  <p>To demonstrate to the world that youngsters unite about the environment, each other and world peace through fund raising and other philanthropic efforts.</p>
</section>

<div class="photo card group" role="img" aria-label="Group of teens in event t-shirts in front of a save the wildlife banner"><span>Lorem ipsum sit amet</span></div>
<div class="photo card founder" role="img" aria-label="Founder standing outdoors in front of green dunes"><span>Lorem ipsum sit amet</span></div>

<div class="social" style="left:758px;top:779px">Subscribe Us on Vidora</div>
<div class="social-mark vidora">Vidora</div>
<div class="social" style="left:788px;top:840px">Like Us on Plixa</div>
<div class="social-mark plixa"><i></i>Plixa</div>
<div class="social-mark helpio"><i></i>Helpio4</div>

<footer class="site-footer">
  <nav><a href="#">Home</a><b>|</b><a href="#">Donate</a><b>|</b><a href="#">Become a sponsor</a><b>|</b><a href="#">How it all got started</a><b>|</b><a href="#">Contact</a></nav>
  <div>© Copyright 2012 Youngsters Unite</div>
</footer>
</body>
</html>
```